The Lantern and the Meadow: Songs Of Quiet Bloom

We need a book cover/spine and back cover for a multi author book called the Lantern and The Meadow: Songs of Quiet Bloom. This will be a collection of stories from women who major transformational stories to tell. They embark on a voyage, find themselves in uncharted territory, find friends or allies and in the end find themselves back home to themselves. I want this book cover to feel fun of wonder, adventure, intrigue with a a dainty energy. I have uploaded some images for inspiration but not to use in the design because they are not images I have permission to use.

```html
<!DOCTYPE html>
<html lang="en">
<head>
<meta charset="utf-8">
<title>The Lantern and the Meadow: Songs Of Quiet Bloom</title>
<link rel="stylesheet" href="https://fonts.googleapis.com/css2?family=Playfair+Display:wght@400&family=DM+Sans:wght@700&display=swap">
<style>
  :root {
    --backdrop: #2f332d;
    --sky: #e4e7e3;
    --haze: #c9d0c4;
    --hills: #9fae98;
    --field: #d8d2bd;
    --bloom: #c9c7ae;
    --stem: #a3ad8a;
    --ink-light: #ffffff;
    --terracotta: #b9653f;
  }
  html, body {
    margin: 0;
    width: 1200px;
    height: 1200px;
    overflow: hidden;
    background: var(--backdrop);
  }
  .book-cover {
    position: absolute;
    left: 286px;
    top: 134px;
    width: 628px;
    height: 944px;
    overflow: hidden;
  }
  .cover-photo {
    position: absolute;
    inset: 0;
    background: linear-gradient(180deg,
      var(--sky) 0%,
      var(--sky) 30%,
      var(--haze) 34%,
      var(--hills) 38%,
      var(--field) 42%,
      var(--bloom) 60%,
      var(--stem) 80%,
      var(--bloom) 100%);
  }
  .cover-title {
    position: absolute;
    inset: 0;
    width: 628px;
    height: 944px;
  }
  .cover-title text {
    font-family: "Playfair Display", "Didot", serif;
    font-weight: 400;
    font-size: 172px;
    letter-spacing: -0.06em;
    fill: var(--ink-light);
  }
  .subtitle-box {
    position: absolute;
    left: 188px;
    top: 820px;
    width: 252px;
    height: 124px;
    background: var(--terracotta);
    display: flex;
    align-items: center;
    justify-content: center;
    text-align: center;
    color: var(--ink-light);
    font-family: "DM Sans", "Helvetica Neue", sans-serif;
    font-weight: 700;
    font-size: 24px;
    line-height: 29px;
    letter-spacing: -0.02em;
    padding-top: 2px;
    box-sizing: border-box;
  }
</style>
</head>
<body>
  <main class="book-cover">
    <div class="cover-photo" role="img" aria-label="Photograph of a woman with long auburn hair seen from behind, standing in a meadow of pale wildflowers under a misty sky"></div>

    <svg class="cover-title" viewBox="0 0 628 944" aria-label="The Lantern and The Meadow">
      <text x="314" y="180" text-anchor="middle">The</text>
      <text x="314" y="338" text-anchor="middle">Lantern</text>
      <text x="314" y="498" text-anchor="middle">and</text>
      <text x="314" y="658" text-anchor="middle">The</text>
      <text x="314" y="818" text-anchor="middle">Meadow</text>
    </svg>

    <div class="subtitle-box">Songs Of<br>Quiet Bloom</div>
  </main>
</body>
</html>
```